YouTube Channel Header Design

YouTube header for company channel. Ridgewell Safety Goods. Looking for technological design for the security industry which includes burglar alarm, fire alarm, cameras, networking and Access Control

```html
<!DOCTYPE html>
<html lang="en">
<head>
<meta charset="utf-8">
<title>Ridgewell Safety Goods – Channel Header Layouts</title>
<link href="https://fonts.googleapis.com/css2?family=Oswald:wght@700&display=swap" rel="stylesheet">
<style>
  :root {
    --page-bg: #e4e4e4;
    --label: #47464a;
    --panel-white: #ffffff;
    --ink: #262c38;
  }
  * { margin: 0; padding: 0; box-sizing: border-box; }
  html, body { width: 1119px; height: 1200px; overflow: hidden; background: var(--page-bg); }
  .canvas { position: relative; width: 1119px; height: 1200px; }

  .device-label {
    position: absolute; left: 0; width: 1119px; text-align: center;
    font-family: "Oswald", "Arial Narrow", sans-serif; font-weight: 700;
    font-size: 36px; letter-spacing: 6px; color: var(--label);
    text-shadow: 0 4px 5px rgba(0,0,0,.45);
  }
  .label-tablet { top: 12px; }
  .label-pc { top: 284px; }
  .label-tv { top: 562px; }

  .banner {
    position: absolute; background: var(--panel-white);
    box-shadow: 0 14px 12px -4px rgba(0,0,0,.55);
    overflow: hidden;
  }
  .banner svg { position: absolute; inset: 0; width: 100%; height: 100%; }
  .banner-tablet { left: 225px; top: 85px; width: 704px; height: 161px; }
  .banner-pc { left: 91px; top: 348px; width: 972px; height: 161px; }
  .banner-tv { left: 107px; top: 623px; width: 940px; height: 529px; }

  .steel { fill: url(#steelGrad); filter: drop-shadow(0 0 4px rgba(0,0,0,.35)); }

  .brand-name {
    position: absolute; width: 509px; transform: translateY(-50%);
    font-family: "Oswald", "Arial Narrow", sans-serif; font-weight: 700;
    color: var(--ink); text-align: center; line-height: 1;
  }
  .brand-name .main { display: block; font-size: 44px; letter-spacing: 5px; }
  .brand-name .sub { display: block; font-size: 17px; letter-spacing: 6px; margin-top: 6px; }
  .banner-tablet .brand-name { left: 71px; top: 80px; }
  .banner-pc .brand-name { left: 205px; top: 80px; }
  .banner-tv .brand-name { left: 204px; top: 274px; }
</style>
</head>
<body>
<div class="canvas">
  <svg width="0" height="0" style="position:absolute">
    <defs>
      <linearGradient id="steelGrad" x1="0" y1="0" x2="1" y2="1">
        <stop offset="0" stop-color="#171b21"/>
        <stop offset="0.5" stop-color="#252c36"/>
        <stop offset="1" stop-color="#1b2027"/>
      </linearGradient>
    </defs>
  </svg>

  <div class="device-label label-tablet">TABLET</div>
  <section class="banner banner-tablet" aria-label="Tablet header">
    <svg viewBox="0 0 1165 266" preserveAspectRatio="none">
      <polygon class="steel" points="20,0 118,0 59,110"/>
      <polygon class="steel" points="0,40 79,266 24,266 0,242"/>
      <polygon class="steel" points="1052,0 1150,0 1113,110"/>
      <polygon class="steel" points="1165,12 1147,266 1092,266 1165,60"/>
      <polygon class="steel" points="1165,20 1165,245 1147,266 1095,266"/>
    </svg>
    <div class="brand-name"><span class="main">RIDGEWELL</span><span class="sub">SAFETY GOODS</span></div>
  </section>

  <div class="device-label label-pc">PC</div>
  <section class="banner banner-pc" aria-label="Desktop header">
    <svg viewBox="0 0 1609 266" preserveAspectRatio="none">
      <polygon class="steel" points="0,0 12,0 0,16"/>
      <polygon class="steel" points="0,52 0,266 196,266"/>
      <polygon class="steel" points="60,0 207,0 301,266 245,266"/>
      <polygon class="steel" points="242,0 340,0 281,110"/>
      <polygon class="steel" points="1274,0 1372,0 1335,110"/>
      <polygon class="steel" points="1549,0 1408,0 1314,266 1370,266"/>
      <polygon class="steel" points="1609,52 1609,266 1418,266"/>
    </svg>
    <div class="brand-name"><span class="main">RIDGEWELL</span><span class="sub">SAFETY GOODS</span></div>
  </section>

  <div class="device-label label-tv">TV</div>
  <section class="banner banner-tv" aria-label="TV header">
    <svg viewBox="0 0 1557 876" preserveAspectRatio="none">
      <polygon class="steel" points="0,0 93,0 333,690 0,312"/>
      <polygon class="steel" points="128,0 517,0 280,428 338,690"/>
      <polygon class="steel" points="0,364 323,728 503,876 0,876"/>
      <polygon fill="#ffffff" points="83,608 323,726 308,728 83,611"/>
      <polygon fill="#ffffff" points="0,748 368,876 342,876 0,758"/>
      <polygon class="steel" points="1557,0 1464,0 1224,690 1557,372"/>
      <polygon class="steel" points="1429,0 1097,0 1335,428 1276,690"/>
      <polygon class="steel" points="1557,424 1290,728 1112,876 1557,876"/>
      <polygon fill="#ffffff" points="1531,608 1290,726 1305,728 1531,611"/>
      <polygon fill="#ffffff" points="1557,768 1248,876 1274,876 1557,778"/>
    </svg>
    <div class="brand-name"><span class="main">RIDGEWELL</span><span class="sub">SAFETY GOODS</span></div>
  </section>
</div>
</body>
</html>
```